Business Card Design Project

I have just chosen a logo and would now like this designed onto a business card for my hair salon. I would like it to be classy not to busy and have a wow factor when people look at them
Has to Include on card:
Logo Design
And business details below
Kellie-ann Drummond (owner)
0482 736 219
Rdw@vomblet.com.au
71 Willowmere Rise Corvin Cove
Logo is now attached please provide designs
Hair

```html
<!DOCTYPE html>
<html lang="en">
<head>
<meta charset="utf-8">
<title>Lumen Hair Studio — Business Card Proposal</title>
<link rel="stylesheet" href="https://fonts.googleapis.com/css2?family=Raleway:wght@300;400;600&display=swap">
<style>
  :root {
    --page: #ffffff;
    --card-dark: #1e1e1e;
    --card-glow: #5a5a5a;
    --pink: #e5097f;
    --cyan: #56c2d0;
    --white: #ffffff;
    --frame-grey: #b5b5b5;
    --sleeve-grey: #e6e6e6;
    --text-light: #e8e8e8;
  }
  * { box-sizing: border-box; margin: 0; padding: 0; }
  html, body { width: 1200px; height: 900px; overflow: hidden; background: var(--page); }
  body { position: relative; font-family: "Raleway", Arial, sans-serif; }

  .card {
    position: absolute;
    background: radial-gradient(ellipse at 45% 55%, var(--card-glow) 0%, #333 30%, var(--card-dark) 70%);
    overflow: hidden;
  }
  .card--front-framed { left: 245px; top: 36px; width: 383px; height: 244px; }
  .card--front-flat   { left: 727px; top: 36px; width: 392px; height: 244px; }
  .card--back-split   { left: 268px; top: 302px; width: 298px; height: 158px;
    background: radial-gradient(ellipse at 50% 80%, #4a4a4a 0%, var(--card-dark) 75%); }
  .card--back-full    { left: 782px; top: 303px; width: 298px; height: 477px;
    background: radial-gradient(ellipse at 50% 40%, #505050 0%, #2c2c2c 40%, var(--card-dark) 80%); }

  .bevel-frame { position: absolute; left: 228px; top: 36px; width: 270px; height: 244px; z-index: 2; }

  .identity { position: absolute; top: 66px; text-align: center; width: 156px; font-weight: 300; }
  .card--front-framed .identity { left: 10px; }
  .card--front-flat .identity { left: 19px; }
  .identity__first { display: block; color: var(--cyan); font-weight: 300; font-size: 21px; letter-spacing: 0.3px; line-height: 26px; }
  .identity__last  { display: block; color: var(--pink); font-weight: 300; font-size: 21px; line-height: 26px; }
  .identity__phone { display: block; color: var(--text-light); font-weight: 400; font-size: 10px; margin-top: 6px; letter-spacing: 0.3px; }

  .divider { position: absolute; top: 64px; width: 2px; height: 72px; background: var(--white); }
  .card--front-framed .divider { left: 172px; }
  .card--front-flat .divider { left: 181px; }

  .contact { position: absolute; top: 70px; color: var(--text-light); font-weight: 300; font-size: 14px; line-height: 21px; font-style: normal; }
  .card--front-framed .contact { left: 181px; }
  .card--front-flat .contact { left: 190px; }

  .swatches { position: absolute; display: flex; gap: 11px; }
  .swatch { width: 16px; height: 16px; }
  .swatch--pink { background: var(--pink); }
  .swatch--white { background: var(--white); }
  .swatch--cyan { background: var(--cyan); }
  .card--front-framed .swatches { left: 130px; top: 201px; }
  .card--front-flat .swatches { left: 139px; top: 201px; }
  .card--back-full .swatches { left: 108px; top: 435px; gap: 14px; }
  .card--back-full .swatch { width: 20px; height: 20px; }

  .brand { position: absolute; color: var(--pink); font-weight: 600; text-transform: uppercase; text-align: center; line-height: 1; }
  .brand--small { font-size: 10px; width: 80px; line-height: 11px; }
  .card--front-framed .brand--small { left: 293px; top: 200px; }
  .card--front-flat .brand--small { left: 302px; top: 200px; }
  .brand--large { left: 0; width: 100%; top: 62px; font-size: 28px; line-height: 34px; letter-spacing: 1px; }

  .sleeve { position: absolute; left: 265px; top: 460px; width: 304px; height: 323px; background: var(--sleeve-grey); }
  .artwork { position: absolute; }
  .artwork--tiles { left: 341px; top: 527px; width: 152px; height: 176px;
    background: linear-gradient(180deg, var(--cyan) 0%, #9a6fc0 40%, var(--pink) 75%, #f4b6d8 100%); opacity: 0.85; }
  .artwork--portrait { left: 68px; top: 205px; width: 125px; height: 194px; border-radius: 50% 50% 40% 40%;
    background: linear-gradient(180deg, var(--cyan) 0%, #9a6fc0 40%, var(--pink) 75%, #f4b6d8 100%); }
</style>
</head>
<body>

  <section class="card card--front-framed" aria-label="Business card front, framed">
    <h1 class="identity">
      <span class="identity__first">KELLIE-ANN</span>
      <span class="identity__last">DRUMMOND</span>
      <span class="identity__phone">0482 736 219</span>
    </h1>
    <div class="divider"></div>
    <address class="contact">Rdw@vomblet.com.au<br>71 Willowmere Rise<br>Corvin Cove</address>
    <div class="swatches"><span class="swatch swatch--pink"></span><span class="swatch swatch--white"></span><span class="swatch swatch--cyan"></span></div>
    <p class="brand brand--small">Lumen Hair Studio</p>
  </section>

  <svg class="bevel-frame" viewBox="0 0 270 244" aria-hidden="true">
    <polygon points="0,0 17,18 17,226 0,244" fill="#8e8e8e"/>
    <polygon points="17,18 17,226 7,236 7,8" fill="#cfcfcf"/>
    <polygon points="0,0 270,0 260,18 17,18" fill="var(--frame-grey)"/>
    <polygon points="0,244 17,226 260,226 270,244" fill="var(--frame-grey)"/>
  </svg>

  <section class="card card--front-flat" aria-label="Business card front">
    <h2 class="identity">
      <span class="identity__first">KELLIE-ANN</span>
      <span class="identity__last">DRUMMOND</span>
      <span class="identity__phone">0482 736 219</span>
    </h2>
    <div class="divider"></div>
    <address class="contact">Rdw@vomblet.com.au<br>71 Willowmere Rise<br>Corvin Cove</address>
    <div class="swatches"><span class="swatch swatch--pink"></span><span class="swatch swatch--white"></span><span class="swatch swatch--cyan"></span></div>
    <p class="brand brand--small">Lumen Hair Studio</p>
  </section>

  <section class="card card--back-split" aria-label="Business card back, top panel">
    <p class="brand brand--large">Lumen<br>Hair Studio</p>
  </section>
  <div class="sleeve"></div>
  <div class="artwork artwork--tiles" role="img" aria-label="Tiled illustration of flowing hair in cyan to pink gradient"></div>

  <section class="card card--back-full" aria-label="Business card back">
    <p class="brand brand--large">Lumen<br>Hair Studio</p>
    <div class="artwork artwork--portrait" role="img" aria-label="Illustration of flowing hair in cyan to pink gradient"></div>
    <div class="swatches"><span class="swatch swatch--pink"></span><span class="swatch swatch--white"></span><span class="swatch swatch--cyan"></span></div>
  </section>

</body>
</html>
```